Webdesign für KFZ-Service-Betrieb
Zielgruppe
Wartung, Reparatur und Instandsetzung von Kraftfahrzeugen aller Marken.
Reifenhandel, Old- und Youngtimer-Service, An- und Verkauf von Fahrzeugen.
Aufgabenstellung
Firmenfarbe ist blau.
Moderner, Übersichtlicher und Transparenter Auftritt erwünscht.

```html
<!DOCTYPE html>
<html lang="de">
<head>
<meta charset="utf-8">
<title>Werkstatt Falkner – KFZ-Service</title>
<link rel="stylesheet" href="https://fonts.googleapis.com/css2?family=Roboto:ital,wght@0,300;0,400;0,500;0,700;1,400;1,500&display=swap">
<style>
:root{
  --blue:#2a2fa4;
  --blue-deep:#23278f;
  --blue-soft:#b3b6e0;
  --ink:#222431;
  --night:#12141f;
  --night-2:#1c1f30;
  --ghost:#f0f0f5;
  --map:#4f5570;
  --footer:#111216;
  --white:#ffffff;
}
*{box-sizing:border-box;margin:0;padding:0}
html,body{width:1200px;height:2906px;overflow:hidden}
body{position:relative;font-family:'Roboto',sans-serif;color:var(--ink);background:var(--white)}
.abs{position:absolute}

/* Hero */
.hero{left:0;top:0;width:1200px;height:599px;background:linear-gradient(100deg,var(--night) 0%,var(--night-2) 55%,#2a2d44 100%)}
.hero-visual{left:560px;top:40px;width:540px;height:540px;border-radius:50%;background:radial-gradient(circle,rgba(90,96,150,.35) 0%,rgba(40,44,70,.15) 60%,rgba(0,0,0,0) 72%)}
.brand{left:232px;top:22px;display:flex;align-items:center;gap:10px;color:var(--white);font-weight:700;font-size:22px}
.brand-dot{width:30px;height:30px;border-radius:50%;background:#4a4fd0}
.nav{top:31px;color:var(--white);font-size:11px;letter-spacing:.2px;text-transform:uppercase}
.hero-bar{left:226px;top:257px;width:4px;height:85px;background:var(--blue)}
.hero-title{left:245px;top:250px;color:var(--white);font-size:43px;font-weight:500;line-height:50px;text-transform:uppercase}
.hero-sub{left:245px;top:355px;color:var(--blue);font-size:29px;font-weight:300}

/* Offer */
.band{left:0;top:599px;width:1200px;height:282px;background:var(--blue)}
.offer{left:226px;top:554px;width:749px;height:378px;background:var(--white);box-shadow:0 6px 18px rgba(0,0,0,.25)}
.offer-ghost{left:300px;top:30px;font-size:96px;font-weight:700;color:var(--ghost);letter-spacing:2px}
.offer-photo{left:12px;top:12px;width:403px;height:353px;background:linear-gradient(110deg,#c9262a 0%,#b9b9bd 40%,#8c8e94 70%,#cfc3a5 100%)}
.offer-bar{left:438px;top:64px;width:2px;height:70px;background:var(--blue)}
.offer-title{left:446px;top:62px;color:var(--blue);font-size:19px;font-weight:500;line-height:25px;text-transform:uppercase}
.offer-text{left:446px;top:158px;font-size:11.3px;line-height:17.5px;color:var(--ink)}
.offer-text p{margin-bottom:17.5px}
.more{left:445px;top:294px;color:var(--blue);font-size:15px;display:flex;align-items:center;gap:5px}

/* Services */
.ghost-title{left:200px;top:1005px;font-size:96px;font-weight:700;color:var(--ghost);letter-spacing:1px}
.service{left:235px;width:360px}
.service h3{color:var(--blue);font-size:19px;font-weight:500;text-transform:uppercase;margin-bottom:14px}
.service p{font-size:11.3px;line-height:17.5px}
.arrow{display:inline-block;vertical-align:middle;margin-left:6px}
.service-bar{left:226px;top:1218px;width:2px;height:38px;background:var(--blue)}
.step{width:32px;height:32px;border-radius:50%;background:#e8e8f4;border:1px solid #d4d5ea;color:#a9abd3;font-size:17px;display:flex;align-items:center;justify-content:center}
.slide{left:658px;top:1152px;width:560px;height:320px;background:var(--white);box-shadow:0 4px 16px rgba(0,0,0,.18)}
.slide-photo{left:12px;top:13px;width:517px;height:295px;background:linear-gradient(120deg,#d8dbe3 0%,#2a3c7a 45%,#1d2c62 70%,#3a3c44 100%)}
.dot{top:1483px;width:8px;height:8px;border-radius:50%;background:#dcdde8}

/* Quote */
.quote{left:0;top:1693px;width:1200px;height:314px;background:linear-gradient(180deg,#2c31aa,var(--blue-deep))}
.quote-text{left:546px;top:1796px;width:430px;color:var(--white);font-style:italic;font-size:15.8px;line-height:25px}
.quote-by{left:900px;top:1884px;width:65px;text-align:right;color:var(--white);font-style:italic;font-weight:500;font-size:15.8px}

/* Map + contact */
.map{left:0;top:2007px;width:1200px;height:413px;background:linear-gradient(135deg,#555b76,var(--map) 60%,#464b64)}
.map-line{left:598px;top:2420px;width:2px;height:39px;background:var(--blue)}
.contact{left:0;top:2478px;width:1200px;text-align:center;color:var(--blue);font-size:15px;line-height:25px}
.contact .gap{height:25px}
.foot-brand{left:0;top:2752px;width:1200px;display:flex;justify-content:center;align-items:center;gap:10px;color:var(--blue);font-weight:700;font-size:24px}
.foot-brand span.mark{width:26px;height:26px;border-radius:50%;background:var(--blue)}
.footer{left:0;top:2863px;width:1200px;height:43px;background:var(--footer);color:var(--white);font-size:8px}
.social{top:18px;width:8px;height:8px;border-radius:50%;background:#c9c9cf}
</style>
</head>
<body>

<section class="abs hero" aria-label="Kopfbereich">
  <div class="abs hero-visual" role="img" aria-label="Technische Zeichnung einer Felge auf dunklem Werkstatthintergrund"></div>
  <div class="abs brand"><span class="brand-dot"></span>Werkstatt Falkner</div>
  <nav>
    <span class="abs nav" style="left:536px">Leistungen</span>
    <span class="abs nav" style="left:651px">Philosophie</span>
    <span class="abs nav" style="left:769px">Firmengeschichte</span>
    <span class="abs nav" style="left:922px">Kontakt</span>
  </nav>
  <div class="abs hero-bar"></div>
  <h1 class="abs hero-title">Wartung, Reparatur<br>&amp; Instandsetzung</h1>
  <p class="abs hero-sub">von Kraftfahrzeugen aller Marken.</p>
</section>

<div class="abs band"></div>
<article class="abs offer">
  <div class="abs offer-ghost">ANGEBOTE</div>
  <div class="abs offer-photo" role="img" aria-label="Foto: Alufelge mit Reifen an einem roten Auto"></div>
  <div class="abs offer-bar"></div>
  <h2 class="abs offer-title">Jetzt günstige<br>Sommerreifen/<br>Sommerräder kaufen!</h2>
  <div class="abs offer-text">
    <p>Bei uns gibt es Markenreifen schon ab 39,- Euro<br>wir liefern alle Fabrikate zu günstigen Preisen.</p>
    <p>Fragen Sie nach Ihren individuellen Angebot.</p>
    <p>Montage-Preis <b>ab 9,50 Euro</b> (pro Rad)<br>Räderwechsel-Preise <b>12,90 / 14,90 / 19,90</b> pro Fahrzeug</p>
  </div>
  <a class="abs more">Mehr
    <svg width="14" height="10" viewBox="0 0 14 10"><path d="M0 5h12M8 1l4 4-4 4" fill="none" stroke="#2a2fa4" stroke-width="1.6"/></svg>
  </a>
</article>

<section aria-label="Leistungen">
  <svg class="abs" style="left:0;top:940px" width="1200" height="760" viewBox="0 940 1200 760">
    <circle cx="829" cy="1320" r="380" fill="none" stroke="#ebebf2" stroke-width="1"/>
    <circle cx="829" cy="1320" r="362" fill="none" stroke="#e6e6ef" stroke-width="1"/>
    <circle cx="829" cy="1316" r="265" fill="none" stroke="#9a9cc4" stroke-width="1" stroke-dasharray="4 4"/>
  </svg>
  <div class="abs ghost-title">LEISTUNGEN</div>

  <div class="abs service" style="top:1128px">
    <h3>Service</h3>
    <p>Bei uns ist nicht nur Ihr Stellaris bestens „aufgehoben“, Wir bieten unsere Service-Leistungen für alle Marken an.<svg class="arrow" width="14" height="10" viewBox="0 0 14 10"><path d="M0 5h12M8 1l4 4-4 4" fill="none" stroke="#2a2fa4" stroke-width="1.6"/></svg></p>
  </div>
  <div class="abs service-bar"></div>
  <div class="abs service" style="top:1227px;width:380px">
    <h3>Unfallinstandsetzung</h3>
    <p>Wir arbeiten nach den vorgeschriebenen Standards der Hersteller.<svg class="arrow" width="14" height="10" viewBox="0 0 14 10"><path d="M0 5h12M8 1l4 4-4 4" fill="none" stroke="#2a2fa4" stroke-width="1.6"/></svg></p>
  </div>
  <div class="abs service" style="top:1306px">
    <h3>Verkauf</h3>
    <p>Wir sind Ihr Ansprechpartner Nr. 1 für Gebrauchtfahrzeuge aller Hersteller - und ganz speziell für „Junge Gebrauchte“.<svg class="arrow" width="14" height="10" viewBox="0 0 14 10"><path d="M0 5h12M8 1l4 4-4 4" fill="none" stroke="#2a2fa4" stroke-width="1.6"/></svg></p>
  </div>
  <div class="abs service" style="top:1406px">
    <h3>Fahrzeugpflege</h3>
    <p>Waschanlage ist nicht gleich Waschanlage! Lackschonende und gründliche Reinigung ist mit unserer Textilflieswaschanlage gewährleistet.<svg class="arrow" width="14" height="10" viewBox="0 0 14 10"><path d="M0 5h12M8 1l4 4-4 4" fill="none" stroke="#2a2fa4" stroke-width="1.6"/></svg></p>
  </div>

  <div class="abs step" style="left:640px;top:1091px">1</div>
  <div class="abs step" style="left:553px;top:1215px">2</div>
  <div class="abs step" style="left:555px;top:1396px">3</div>
  <div class="abs step" style="left:639px;top:1506px">4</div>

  <div class="abs slide">
    <div class="abs slide-photo" role="img" aria-label="Foto: Mechaniker in blauer Arbeitskleidung wechselt ein Rad"></div>
  </div>
  <span class="abs dot" style="left:658px;background:var(--blue)"></span>
  <span class="abs dot" style="left:675px"></span>
  <span class="abs dot" style="left:692px"></span>
  <span class="abs dot" style="left:710px"></span>
</section>

<section class="abs quote" role="img" aria-label="Kundenstimme vor blau getöntem Armaturenbrett">
  <svg class="abs" style="left:302px;top:95px" width="156" height="124" viewBox="0 0 156 124">
    <path d="M36 124c-20 0-36-16-36-38C0 42 28 8 62 0l6 10C44 20 30 38 30 52c4-2 8-3 12-3 19 0 34 15 34 37s-17 38-40 38z" fill="#b3b6e0"/>
    <path d="M116 124c-20 0-36-16-36-38C80 42 108 8 142 0l6 10c-24 10-38 28-38 42 4-2 8-3 12-3 19 0 34 15 34 37s-17 38-40 38z" fill="#b3b6e0"/>
  </svg>
</section>
<blockquote class="abs quote-text">Ich möchte mich noch einmal ausdrücklich für Ihre jahrelang erbrachten exzellenten Dienstleistungen bedanken und wünsche dem gesamten Team weiterhin alles Gute!</blockquote>
<div class="abs quote-by">K.L.</div>

<div class="abs map" role="img" aria-label="Stadtplan von Berlin mit Standort der Werkstatt"></div>
<div class="abs map-line"></div>
<address class="abs contact" style="font-style:normal">
  Lindenhofstraße 42<br>10969 Berlin
  <div class="gap"></div>
  <strong style="font-weight:500">ÖFFNUNGSZEITEN:</strong><br>
  Mo.-Fr.: 07.30 Uhr - 18.00 Uhr<br>
  Sa.: 09.00 Uhr-12.00 Uhr<br>
  Telefon:030/5550120<br>
  Telefax:030/5550121
</address>

<div class="abs foot-brand"><span class="mark"></span>Werkstatt Falkner</div>

<footer class="abs footer">
  <span class="abs social" style="left:233px"></span>
  <span class="abs social" style="left:253px"></span>
  <span class="abs social" style="left:273px"></span>
  <span class="abs" style="left:297px;top:17px">Autoservice nach Maß</span>
  <span class="abs" style="left:800px;top:17px;width:165px;text-align:right">Werkstatt Falkner © Copyright 2016</span>
</footer>

</body>
</html>
```